Catering Company Needs a Web Page Design

I already have my logo, and so I'm moving onto the next phase.. the web page design. Platrix is a gourmet catering company based in orlando, fl, set to launch in 2015. I will have a store location to host cooking classes as well.... and will be uploading cooking demo videos to my website weekly. Id like a blog section, and about, a video section, contact form, Services, Menu Samples..... My logo and concept is modern, innovative, and fun! I am targeting middle class to upper middle class women, but i want the site to be super unique.

Industry/Entity Type

Catering

Requirements
Must have
• The front/main page must have the logo... and the lingo ledger's definition of "platrix". I like movement... maybe the top banner can move somehow.. Im not a web designer, so i wont really know until I start seeing some examples. For now I dont have photos of my own cooking, so if you could use stock photos of catering dishes.. I uploaded a transparent logo also, maybe that could be the top banner placed over a scene of expertly plated hordourves...

```html
<!DOCTYPE html>
<html lang="en">
<head>
<meta charset="utf-8">
<title>Platrix — Gourmet Catering &amp; Cooking Classes</title>
<link href="https://fonts.googleapis.com/css2?family=Open+Sans:wght@300;400;600;700&display=swap" rel="stylesheet">
<style>
:root{
  --orange:#f08a00;
  --green:#7ab32e;
  --ink:#333;
  --body:#444;
  --rule:#e2e2e2;
  --panel:#f6f6f6;
  --footer:#efefef;
}
*{box-sizing:border-box;margin:0;padding:0}
html,body{width:1058px;height:1200px;overflow:hidden;background:#fff;font-family:"Open Sans",Arial,sans-serif;color:var(--ink)}
.page{position:relative;width:1058px;height:1200px}
.abs{position:absolute}

/* header */
.brand{left:113px;top:10px}
.brand-name{font-size:50px;font-weight:700;color:#3d3d3d;line-height:1;letter-spacing:-1px;display:flex;align-items:center;gap:8px}
.brand-dot{width:14px;height:14px;border-radius:50%;background:var(--orange)}
.brand-tag{font-size:8.5px;color:#666;margin-left:44px;margin-top:4px}
.nav a{position:absolute;top:43px;font-size:16px;color:var(--ink);text-decoration:none}
.nav .active::after{content:"";position:absolute;left:-11px;right:-8px;top:29px;height:3px;background:var(--orange)}

/* hero */
.hero{left:0;top:86px;width:1058px;height:353px;
  background:radial-gradient(ellipse at 52% 38%,#e88a4e 0%,#d97a3e 18%,#c9a36a 34%,#9fb35a 50%,#dfe6df 72%,#eef0f0 100%)}
.definition{left:113px;top:206px;width:318px;height:113px;background:rgba(70,70,70,.78);color:#fff;padding:8px 14px}
.definition h1{font-size:18px;font-weight:400;line-height:1.3}
.definition h1 b{font-weight:700}
.definition h1 i{color:var(--orange);font-weight:700}
.definition p{font-size:15.5px;font-weight:300;line-height:21px;margin-top:5px}
.dots{left:435px;top:400px;display:flex;gap:6px}
.dots span{width:13px;height:13px;border-radius:50%;background:#fff}
.dots span:first-child{background:#333}

.contact{left:707px;top:104px;width:237px;height:321px;background:var(--panel)}
.contact h2{height:41px;background:var(--green);color:#fff;font-weight:400;font-size:16px;padding:11px 12px}
.field{position:absolute;left:12px;width:210px;background:#fff;font-size:9px;color:#999;padding:11px 7px}
.submit{position:absolute;left:65px;top:280px;width:91px;height:25px;background:var(--orange);color:#fff;font-weight:700;font-size:15px;text-align:center;line-height:25px}

/* sections */
.heading{font-size:16px;font-weight:700;color:var(--orange)}
.thumb{width:196px;height:114px}
.post-text{left:326px;width:336px;font-size:10px;line-height:21px;color:var(--body)}
.post-text h3{font-size:10.5px;font-weight:700;color:#222}
.rule{left:113px;width:547px;height:1px;background:var(--rule)}
.share{left:117px;display:flex;gap:7px}
.share span{font-size:9.5px;font-weight:600;border:1px solid #ccc;border-radius:2px;padding:1px 5px;background:#fafafa;color:#333}
.share .gp{color:#c33}.share .pin{color:#b22}.share .lk{color:#3b5998}
.more{left:560px;width:100px;text-align:right;font-size:10.5px;font-weight:700;color:#222}

.video{left:682px;width:262px;height:139px;background:#fff;border:1px solid #ddd;box-shadow:0 1px 3px rgba(0,0,0,.15);padding:4px}
.video .shot{width:100%;height:100%;position:relative}
.play{position:absolute;left:50%;top:50%;width:40px;height:40px;margin:-20px;border-radius:50%;background:#444;border:2px solid #eee}
.play::after{content:"";position:absolute;left:15px;top:11px;border-left:13px solid #fff;border-top:8px solid transparent;border-bottom:8px solid transparent}
.caption{left:682px;width:264px;font-size:10px;line-height:21px;color:var(--body)}

/* footer */
.footer{left:0;top:1122px;width:1058px;height:78px;background:var(--footer)}
.footnav{left:111px;top:1133px;font-size:12.5px;color:#333;word-spacing:2px}
.footnav i{font-style:normal;margin:0 18px}
.copy{left:112px;top:1162px;font-size:12.5px;color:#333}
.social{top:1143px;width:36px;height:36px;border-radius:50%;background:#4a4a4a}
</style>
</head>
<body>
<div class="page">

  <header>
    <div class="abs brand">
      <div class="brand-name"><span class="brand-dot"></span>platrix</div>
      <div class="brand-tag">Gourmet Catering &amp; Cooking Classes</div>
    </div>
    <nav class="nav">
      <a class="active" style="left:393px">Home</a>
      <a style="left:484px">About Us</a>
      <a style="left:600px">Services</a>
      <a style="left:712px">Videos</a>
      <a style="left:787px">Blog</a>
      <a style="left:862px">Contact Us</a>
    </nav>
  </header>

  <section class="abs hero" role="img" aria-label="Banner photo of grilled salmon with asparagus and snap peas on a white plate"></section>
  <div class="abs definition">
    <h1><b>platrix</b> (plat-rix) <i>noun</i></h1>
    <p>Those who are overly zealous and enthusiastic about cooking, eating, and fine dining</p>
  </div>
  <div class="abs dots"><span></span><span></span><span></span><span></span></div>

  <form class="abs contact">
    <h2>Contact Us</h2>
    <div class="field" style="top:61px;height:33px">Name</div>
    <div class="field" style="top:101px;height:33px">E-Mail</div>
    <div class="field" style="top:143px;height:33px">Phone</div>
    <div class="field" style="top:187px;height:68px">Message</div>
    <div class="submit">Submit</div>
  </form>

  <h2 class="abs heading" style="left:111px;top:493px">Blog</h2>
  <h2 class="abs heading" style="left:680px;top:493px">Videos</h2>

  <!-- blog posts -->
  <div class="abs thumb" style="left:113px;top:535px;background:linear-gradient(135deg,#e9ecef,#c9d3cf 45%,#b86c4a 60%,#eef0f2)" role="img" aria-label="Grilled chicken salad on a white plate"></div>
  <article class="abs post-text" style="top:530px">
    <h3>Sed ut perspiciatis unde omnis iste natus error sit voluptatem accusantium doloremque laudantium</h3>
    <p>Totam rem aperiam, eaque ipsa quae ab illo inventore veritatis et quasi architecto beatae vitae dicta sunt explicabo. Nemo enim ipsam voluptatem quia voluptas sit aspernatur aut odit aut fugit, sed quia consequuntur magni dolores eos qui ratione</p>
  </article>
  <div class="abs rule" style="top:666px"></div>
  <div class="abs share" style="top:676px"><span>Tweet</span><span class="gp">+1</span><span class="pin">Pin it</span><span class="lk">Like</span></div>
  <div class="abs more" style="top:677px">Read More &gt;&gt;</div>
  <div class="abs rule" style="top:703px"></div>

  <div class="abs thumb" style="left:113px;top:726px;background:linear-gradient(120deg,#d9a46a,#e9c79a 50%,#c98a52)" role="img" aria-label="Couple enjoying a meal together at a kitchen table"></div>
  <article class="abs post-text" style="top:720px">
    <h3>Sed ut perspiciatis unde omnis iste natus error sit voluptatem accusantium doloremque laudantium</h3>
    <p>Totam rem aperiam, eaque ipsa quae ab illo inventore veritatis et quasi architecto beatae vitae dicta sunt explicabo. Nemo enim ipsam voluptatem quia voluptas sit aspernatur aut odit aut fugit, sed quia consequuntur magni dolores eos qui ratione</p>
  </article>
  <div class="abs rule" style="top:862px"></div>
  <div class="abs share" style="top:875px"><span>Tweet</span><span class="gp">+1</span><span class="pin">Pin it</span><span class="lk">Like</span></div>
  <div class="abs more" style="top:876px">Read More &gt;&gt;</div>
  <div class="abs rule" style="top:903px"></div>

  <div class="abs thumb" style="left:113px;top:915px;background:radial-gradient(ellipse at 45% 50%,#6aa53a,#c8402e 65%,#e34b3a 80%,#fff 95%)" role="img" aria-label="Fresh fruit and greens salad in a red bowl"></div>
  <article class="abs post-text" style="top:910px">
    <h3>Sed ut perspiciatis unde omnis iste natus error sit voluptatem accusantium doloremque laudantium</h3>
    <p>Totam rem aperiam, eaque ipsa quae ab illo inventore veritatis et quasi architecto beatae vitae dicta sunt explicabo. Nemo enim ipsam voluptatem quia voluptas sit aspernatur aut odit aut fugit, sed quia consequuntur magni dolores eos qui ratione</p>
  </article>
  <div class="abs rule" style="top:1041px"></div>
  <div class="abs share" style="top:1054px"><span>Tweet</span><span class="gp">+1</span><span class="pin">Pin it</span><span class="lk">Like</span></div>
  <div class="abs more" style="top:1055px">Read More &gt;&gt;</div>
  <div class="abs rule" style="top:1085px"></div>

  <!-- videos -->
  <div class="abs video" style="top:538px"><div class="shot" role="img" aria-label="Video still of a plated fish dish with wine glasses in a restaurant" style="background:linear-gradient(180deg,#8a5a34,#c9a27a 55%,#eee 80%)"><span class="play"></span></div></div>
  <p class="abs caption" style="top:682px">Totam rem aperiam, eaque ipsa quae ab illo inventore veritatis</p>
  <div class="abs video" style="top:728px"><div class="shot" role="img" aria-label="Video still of quesadillas with a dip and fresh herbs" style="background:linear-gradient(135deg,#e6d6bc,#f4efe6 45%,#7f9a45 65%,#c89a62)"><span class="play"></span></div></div>
  <p class="abs caption" style="top:873px">Totam rem aperiam, eaque ipsa quae ab illo inventore veritatis</p>
  <div class="abs video" style="top:926px"><div class="shot" role="img" aria-label="Video still of roasted peppers and vegetables in a pan" style="background:radial-gradient(ellipse at 50% 60%,#d23a22,#8a2a1a 55%,#2d2a24 75%,#c89a52)"><span class="play"></span></div></div>
  <p class="abs caption" style="top:1073px">Totam rem aperiam, eaque ipsa quae ab illo inventore veritatis</p>

  <footer>
    <div class="abs footer"></div>
    <div class="abs footnav">Home<i>|</i>About Us<i>|</i>Services<i>|</i>Videos<i style="margin:0 10px">|</i>Blog<i>|</i>Contact Us</div>
    <div class="abs copy">© 2014 Company Name All Rights reserved</div>
    <span class="abs social" style="left:864px" aria-label="Social link"></span>
    <span class="abs social" style="left:908px" aria-label="Social link"></span>
  </footer>
</div>
</body>
</html>
```